New business card for civil engineering company - "Keystone Audit"

We need a business card designed for our new structural engineering company.

The company name is "Keystone Audit" logo files attached.

We would like the following:
* Two-sided card
* Simple design

Information to be placed on the card:
Name - Marcus Dellow
Job Title - Director / Structural Engineer
Credentials - BEng(Hons), CPEng, CMengNZ, IntPE(NZ)
Email - marcus.dellow@keystoneaudit.co.nz
mobile - 0219364058
website - www.keystoneaudit.co.nz

```html
<!DOCTYPE html>
<html lang="en">
<head>
<meta charset="utf-8">
<title>Keystone Audit — Business Card</title>
<link href="https://fonts.googleapis.com/css2?family=Montserrat:wght@500;800&family=Arimo:wght@400;700&display=swap" rel="stylesheet">
<style>
  :root {
    --ink: #231f20;
    --ink-soft: #6d6e71;
    --blue-deep: #3f8fcb;
    --blue-light: #aadcf2;
    --blue-label: #1f72bb;
    --divider: #5f9fd3;
    --paper-start: #ffffff;
    --paper-end: #e4e4e7;
    --page: #ffffff;
    --clear: rgba(170, 220, 242, 0);
  }
  * { box-sizing: border-box; margin: 0; padding: 0; }
  html, body { width: 1200px; height: 1000px; overflow: hidden; background: var(--page); }
  .sheet { position: relative; width: 1200px; height: 1000px; }

  .card {
    position: absolute;
    width: 711px; height: 407px;
    border: 1px solid var(--blue-label);
    background: linear-gradient(120deg, var(--paper-start) 20%, var(--paper-end) 100%);
    overflow: hidden;
  }
  .card--front { left: 243px; top: 71px; }
  .card--back  { left: 244px; top: 521px; }

  /* Soft colour fields where the corner decoration sits */
  .accent { position: absolute; }
  .accent--top-left {
    left: 0; top: 0; width: 262px; height: 182px;
    background: linear-gradient(145deg, var(--blue-deep) 0%, var(--blue-light) 40%, var(--clear) 70%);
  }
  .accent--bottom-right {
    right: 0; bottom: 0; width: 262px; height: 182px;
    background: linear-gradient(325deg, var(--blue-deep) 0%, var(--blue-light) 40%, var(--clear) 70%);
  }
  .accent--top-right {
    right: 0; top: 0; width: 180px; height: 260px;
    background: linear-gradient(220deg, var(--blue-deep) 0%, var(--blue-light) 40%, var(--clear) 70%);
  }
  .accent--bottom-left {
    left: 0; bottom: 0; width: 180px; height: 260px;
    background: linear-gradient(40deg, var(--blue-deep) 0%, var(--blue-light) 40%, var(--clear) 70%);
  }

  .wordmark {
    position: absolute;
    font-family: "Montserrat", sans-serif;
    font-weight: 500;
    color: var(--ink);
    letter-spacing: 0.1em;
    white-space: nowrap;
    line-height: 1;
    transform: translateX(-50%);
  }
  .tagline {
    position: absolute;
    font-family: "Arimo", sans-serif;
    color: var(--ink-soft);
    letter-spacing: 0.32em;
    white-space: nowrap;
    line-height: 1;
    transform: translateX(-50%);
  }
  .card--front .wordmark { left: 50%; top: 281px; font-size: 24px; }
  .card--front .tagline  { left: 50%; top: 313px; font-size: 10px; }
  .card--back .wordmark  { left: 181px; top: 268px; font-size: 16px; }
  .card--back .tagline   { left: 181px; top: 289px; font-size: 7.5px; letter-spacing: 0.3em; }

  .divider {
    position: absolute; left: 310px; top: 91px;
    width: 4px; height: 228px; background: var(--divider);
  }
  .person__name {
    position: absolute; left: 343px; top: 98px;
    font-family: "Montserrat", sans-serif; font-weight: 800;
    font-size: 38px; line-height: 31px; color: var(--ink);
    letter-spacing: -0.01em;
  }
  .person__role {
    position: absolute; left: 343px; top: 168px;
    height: 17px; padding: 0 4px;
    background: var(--blue-label); color: #fff;
    font-family: "Arimo", sans-serif; font-weight: 700;
    font-size: 11.5px; line-height: 17px; letter-spacing: 0.05em;
    white-space: nowrap;
  }
  .credentials {
    position: absolute; left: 341px; top: 216px;
    font-family: "Arimo", sans-serif; font-weight: 700;
    font-size: 9px; line-height: 12px; letter-spacing: 0.09em;
    color: var(--ink); white-space: nowrap;
  }
  .contact { position: absolute; left: 344px; top: 247px; list-style: none; }
  .contact__item {
    display: flex; align-items: center; gap: 7px;
    height: 21px;
    font-family: "Arimo", sans-serif; font-weight: 400;
    font-size: 9px; letter-spacing: 0.09em; color: var(--ink);
    white-space: nowrap;
  }
  .contact__icon { width: 12px; height: 12px; flex: none; fill: var(--blue-label); }
</style>
</head>
<body>
<main class="sheet">

  <section class="card card--front" aria-label="Card front">
    <div class="accent accent--top-left" role="img" aria-label="Blue corner decoration"></div>
    <div class="accent accent--top-right" role="img" aria-label="Blue edge decoration"></div>
    <div class="accent accent--bottom-left" role="img" aria-label="Blue edge decoration"></div>
    <div class="accent accent--bottom-right" role="img" aria-label="Blue corner decoration"></div>
    <p class="wordmark">KEYSTONE AUDIT</p>
    <p class="tagline">PEER REVIEW SPECIALISTS</p>
  </section>

  <section class="card card--back" aria-label="Card back">
    <div class="accent accent--top-left" role="img" aria-label="Blue corner decoration"></div>
    <div class="accent accent--bottom-right" role="img" aria-label="Blue corner decoration"></div>

    <p class="wordmark">KEYSTONE AUDIT</p>
    <p class="tagline">PEER REVIEW SPECIALISTS</p>

    <div class="divider"></div>

    <h1 class="person__name">MARCUS<br>DELLOW</h1>
    <p class="person__role">DIRECTOR / STRUCTURAL ENGINEER</p>

    <p class="credentials">CREDENTIALS<br>BENG(HONS), CPENG, CMENGNZ, INTPE(NZ)</p>

    <ul class="contact">
      <li class="contact__item">
        <svg class="contact__icon" viewBox="0 0 24 24" aria-hidden="true"><path d="M1 4h22v16H1z" fill="var(--blue-label)"/><path d="M2 5l10 8 10-8M2 19l8-7M22 19l-8-7" stroke="#fff" stroke-width="1.6" fill="none"/></svg>
        <span>MARCUS.DELLOW@KEYSTONEAUDIT.CO.NZ</span>
      </li>
      <li class="contact__item">
        <svg class="contact__icon" viewBox="0 0 24 24" aria-hidden="true"><path d="M6.6 10.8a15.2 15.2 0 0 0 6.6 6.6l2.2-2.2c.3-.3.7-.4 1-.2 1.1.4 2.3.6 3.6.6.6 0 1 .4 1 1V20c0 .6-.4 1-1 1C10.6 21 3 13.4 3 4c0-.6.4-1 1-1h3.5c.6 0 1 .4 1 1 0 1.3.2 2.5.6 3.6.1.3 0 .7-.2 1z"/></svg>
        <span>0219364058</span>
      </li>
      <li class="contact__item">
        <svg class="contact__icon" viewBox="0 0 24 24" aria-hidden="true"><circle cx="12" cy="12" r="10.5"/><g stroke="#fff" stroke-width="1.4" fill="none"><ellipse cx="12" cy="12" rx="4.5" ry="10"/><path d="M2 12h20M3.5 7h17M3.5 17h17M12 2v20"/></g></svg>
        <span>WWW.KEYSTONEAUDIT.CO.NZ</span>
      </li>
    </ul>
  </section>

</main>
</body>
</html>
```